Financial Advisor Resource Firm needs business card design

Need business card design for company in Omaha NE called Tallowbrook Partners. We provide resources to financial advisors....workshop programs, retirement analysis, and insurance planning. I would like to see designs that use grays, greens, black, and white colors. The final design should communicate 'collaboration' and be simple yet attractive to financial planning clients. I will attached our logo and another picture of a puzzle piece coming together. I would like the incorporate the puzzle picture somehow, maybe on the back somehow, with color or just the gray scale....OR, the picture be the front of the card with 'Tallowbrook' definition on it (see upload) and then company logo, employee name, title, address on the back (see ppt uploaded). The following disclosure needs to be included somewhere- Advisory services offered through Marlowe Ridge Advisors, LLC.
Updates

I uploaded a svg and ai file of the logo

Target Market(s)

Financial planning clients and financial advisors....so pretty diverse age range of about 40-70.

Industry/Entity Type

Financial Planning

Contact Information for Business Card

Dennis K. Holloway, MBA
Founder/President
5727 E. Larkspur Avenue
Suite 418
Omaha, NE 68297
Phone- (402) 555-0147
Cell- (402) 555-0183
Fax- (402) 555-0129
email- dennis@tallowbrookgroup.example
web address- www.tallowbrookgroup.example

Colors
1b1b1b
474747
d3d3d3
ffffff
9bcb3c
abd036

Requirements
Must have
• Must include logo provided, must be 2 sided, and must have disclosure...all of these items listed in project description

```html
<!DOCTYPE html>
<html lang="en">
<head>
<meta charset="utf-8">
<title>Tallowbrook Partners – Business Card</title>
<link rel="stylesheet" href="https://fonts.googleapis.com/css2?family=Merriweather:wght@400;700&family=Roboto:wght@400;500;700&display=swap">
<style>
  :root {
    --ink: #1b1b1b;
    --charcoal: #474747;
    --silver: #d3d3d3;
    --paper: #ffffff;
    --green: #9bcb3c;
    --green-bright: #abd036;
    --backdrop: #2e3236;
  }
  * { box-sizing: border-box; margin: 0; padding: 0; }
  html, body { width: 1200px; height: 900px; overflow: hidden; }
  body {
    background: var(--backdrop);
    font-family: "Roboto", Arial, sans-serif;
    position: relative;
  }
  .card {
    position: absolute;
    left: 260px;
    width: 680px;
    height: 388px;
    border-radius: 22px;
    overflow: hidden;
    box-shadow: 0 10px 30px rgba(0,0,0,.45);
  }
  .card--definition { top: 36px; }
  .card--contact { top: 476px; background: var(--ink); }

  /* Definition side */
  .photo-fill {
    position: absolute; inset: 0;
    background: linear-gradient(115deg, #f2f2f2 0%, #c9c9c9 30%, #8a8a8a 58%, #4a4a4a 82%, #2b2b2b 100%);
  }
  .word-tab {
    position: absolute; left: 0; top: 118px;
    width: 300px; height: 62px;
  }
  .word-tab svg { position: absolute; inset: 0; }
  .word-tab__label {
    position: absolute; left: 28px; top: 0; line-height: 62px;
    font-family: "Merriweather", Georgia, serif;
    font-weight: 700; font-size: 27px; letter-spacing: 1px;
    color: var(--paper); text-transform: uppercase;
  }
  .definition {
    position: absolute; left: 318px; top: 176px; width: 330px;
    font-size: 21px; font-weight: 500; line-height: 1.3;
    color: var(--green-bright);
  }
  .brand {
    position: absolute; display: flex; align-items: center; gap: 12px;
    font-family: "Merriweather", Georgia, serif; font-weight: 400;
    color: var(--ink); text-transform: uppercase; letter-spacing: 2px;
  }
  .brand__dot { border-radius: 50%; background: var(--green); flex: none; }
  .card--definition .brand { left: 220px; top: 38px; font-size: 34px; }
  .card--definition .brand__dot { width: 26px; height: 26px; }

  /* Contact side */
  .contact-top { position: absolute; left: 0; top: 0; width: 680px; height: 250px; background: var(--paper); }
  .card--contact .brand { left: 0; right: 0; top: 62px; justify-content: center; font-size: 33px; }
  .card--contact .brand__dot { width: 24px; height: 24px; }
  .band { position: absolute; left: 0; top: 0; }
  .holder {
    position: absolute; left: 26px; top: 170px;
    color: var(--ink);
  }
  .holder__name { font-family: "Merriweather", Georgia, serif; font-weight: 700; font-size: 21px; }
  .holder__title { font-size: 15px; margin-top: 6px; }
  .web {
    position: absolute; right: 28px; top: 214px;
    font-weight: 700; font-size: 17px; color: var(--ink);
  }
  .lines {
    position: absolute; left: 26px; top: 270px; list-style: none;
    color: var(--paper); font-size: 15px;
  }
  .lines li { display: flex; align-items: center; gap: 10px; height: 24px; }
  .lines svg { width: 15px; height: 15px; flex: none; }
  .office {
    position: absolute; right: 28px; top: 270px; text-align: right;
    color: var(--paper); font-size: 16px; line-height: 1.4;
  }
  .office__note { font-weight: 700; margin-bottom: 10px; }
</style>
</head>
<body>

<section class="card card--definition">
  <div class="photo-fill" role="img" aria-label="Grayscale photo of hands fitting puzzle pieces together"></div>
  <div class="brand"><span class="brand__dot"></span>Tallowbrook Partners</div>
  <div class="word-tab">
    <svg width="300" height="62" viewBox="0 0 300 62" aria-hidden="true">
      <polygon points="0,0 272,0 300,31 272,62 0,62" fill="var(--green)"/>
    </svg>
    <span class="word-tab__label">Tallowbrook</span>
  </div>
  <p class="definition">to come together and unite in common interest and focus.</p>
</section>

<section class="card card--contact">
  <div class="contact-top"></div>
  <svg class="band" width="680" height="388" viewBox="0 0 680 388" aria-hidden="true">
    <polygon points="0,160 300,160 336,202 680,202 680,250 0,250" fill="var(--green)"/>
  </svg>
  <div class="brand"><span class="brand__dot"></span>Tallowbrook Partners</div>
  <div class="holder">
    <div class="holder__name">Dennis K. Holloway, MBA</div>
    <div class="holder__title">Founder/President</div>
  </div>
  <div class="web">www.tallowbrookgroup.example</div>

  <ul class="lines">
    <li>
      <svg viewBox="0 0 16 16" aria-hidden="true"><path d="M3 1h3l1 4-2 1a8 8 0 0 0 5 5l1-2 4 1v3a2 2 0 0 1-2 2A13 13 0 0 1 1 3a2 2 0 0 1 2-2z" fill="var(--green)"/></svg>
      (402) 555-0147
    </li>
    <li>
      <svg viewBox="0 0 16 16" aria-hidden="true"><rect x="4" y="1" width="8" height="14" rx="1.5" fill="none" stroke="var(--green)" stroke-width="1.6"/></svg>
      (402) 555-0183
    </li>
    <li>
      <svg viewBox="0 0 16 16" aria-hidden="true"><rect x="1" y="6" width="14" height="8" rx="1" fill="var(--green)"/><rect x="4" y="1" width="8" height="6" fill="none" stroke="var(--green)" stroke-width="1.5"/></svg>
      (402) 555-0129
    </li>
    <li>
      <svg viewBox="0 0 16 16" aria-hidden="true"><rect x="1" y="3" width="14" height="10" fill="var(--green)"/><path d="M1 3l7 6 7-6" fill="none" stroke="var(--ink)" stroke-width="1.4"/></svg>
      dennis@tallowbrookgroup.example
    </li>
  </ul>

  <div class="office">
    <p class="office__note">Advisory services offered<br>through Marlowe Ridge Advisors, LLC.</p>
    <p>5727 E. Larkspur Avenue<br>Suite 418, Omaha, NE 68297</p>
  </div>
</section>

</body>
</html>
```